Flyer Design Project

I need a flyer design to attract people to rent our Condo in Steamboat. Looking for A5 double sided with something that will really excite people to rent it over winter. FLYER IS ONLY FOR CONDO NOT THE BELLWOOD AS A WHOLE.

Reason: Hi just waiting on a response

Requirements
Must have
• Lots of great pictures contact details bellwood5e@examplemail.net
Include rank no 1 on staywander
Access photos here

https://www.filecrate.net/home/Photos/Bellwood%205E%20-%20High%20Res%20Print%20Ready

Access video here
http://www.vidloop.net/watch?v=Q_kkwaPnmRT&feature=vl.be

Here is bellwood website

http://www.bellwoodretreat.net/

```html
<!DOCTYPE html>
<html lang="en">
<head>
<meta charset="utf-8">
<title>Condo 5E – Come stay</title>
<link rel="stylesheet" href="https://fonts.googleapis.com/css2?family=Pinyon+Script&family=Roboto+Condensed:wght@300;400&display=swap">
<style>
  :root {
    --surround: #3f2a1f;
    --surround-dark: #2e1d15;
    --card-light: #f6f3ec;
    --card-mid: #e6ddcc;
    --card-deep: #cbbda3;
    --text: #5a5550;
    --title: #3b3632;
    --accent: #8a6a3a;
    --photo-warm: #b88a4e;
    --photo-deep: #6e4a2a;
  }
  * { margin: 0; padding: 0; box-sizing: border-box; }
  html, body {
    width: 1200px; height: 846px; overflow: hidden;
    background: radial-gradient(ellipse at center, var(--surround) 0%, var(--surround-dark) 100%);
  }
  .flyer {
    position: absolute; left: 86px; top: 57px; width: 1029px; height: 730px;
    background: linear-gradient(135deg, var(--card-deep) 0%, var(--card-mid) 30%, var(--card-light) 60%, var(--card-light) 100%);
    overflow: hidden;
    font-family: "Roboto Condensed", "Arial Narrow", sans-serif;
    font-weight: 300; color: var(--text);
  }
  .hero-skier {
    position: absolute; left: 0; top: 0; width: 420px; height: 400px;
    background: radial-gradient(ellipse at 35% 35%, rgba(150,130,100,.45) 0%, rgba(200,185,160,.25) 45%, rgba(246,243,236,0) 75%);
  }
  .hero-couple {
    position: absolute; left: 690px; top: 330px; width: 339px; height: 400px;
    background: radial-gradient(ellipse at 55% 40%, rgba(190,165,130,.6) 0%, rgba(214,200,176,.4) 50%, rgba(246,243,236,0) 85%);
  }
  .title {
    position: absolute; left: 418px; top: 28px;
    font-family: "Pinyon Script", cursive; font-weight: 400;
    font-size: 66px; line-height: 1.3; color: var(--title); letter-spacing: 1px;
  }
  .intro {
    position: absolute; left: 424px; top: 146px; width: 566px;
    font-size: 15px; line-height: 22px;
  }
  .intro p + p { margin-top: 22px; }
  .gallery {
    position: absolute; left: 0; top: 393px; display: flex; gap: 7px;
  }
  .gallery .room {
    height: 170px;
    background: linear-gradient(160deg, var(--photo-warm) 0%, #a2774a 45%, var(--photo-deep) 100%);
  }
  .room-bath { width: 136px; }
  .room-bed1 { width: 132px; }
  .room-bed2 { width: 132px; }
  .room-spa { width: 132px; }
  .room-bed3 { width: 132px; }
  .booking {
    position: absolute; left: 424px; top: 595px; width: 566px;
    font-size: 15px; line-height: 22px;
  }
  .booking .tour { margin-top: 22px; }
  .ranking {
    position: absolute; left: 46px; top: 640px;
    display: flex; align-items: center; gap: 8px;
    font-size: 18px; font-weight: 400; color: var(--title);
  }
  .ranking .brand { font-size: 25px; color: var(--accent); font-weight: 400; }
  .ranking .dot { width: 16px; height: 16px; border-radius: 50%; background: var(--accent); }
</style>
</head>
<body>
  <main class="flyer">
    <div class="hero-skier" role="img" aria-label="Faded photo of a skier jumping through powder snow"></div>
    <div class="hero-couple" role="img" aria-label="Faded photo of a smiling couple in winter clothing"></div>

    <h1 class="title">Come stay...</h1>

    <section class="intro">
      <p>From the comfort of the Bellwood - you can enjoy a unique and memorable vacation in this magical place.</p>
      <p>Condo 5E is a subpenthouse suite with 2000 square-feet of luxury accommodation which boasts four bedrooms and three and a half bathrooms. Here you will find everything need during your ultimate Colorado vacation including a gourmet kitchen, spacious living area, built-in fireplace, full size washer and dryer, luxury linen, daily cleaning service, five flat panel TV’s, complimentary wireless internet and private balconies. Also enjoy the facilities of the Bellwood including private health and fitness club, indoor-outdoor heated pool, ski valet service and a concierge to handle your personal requests.</p>
    </section>

    <section class="gallery">
      <div class="room room-bath" role="img" aria-label="Photo of the bathroom vanity"></div>
      <div class="room room-bed1" role="img" aria-label="Photo of a bedroom with a double bed"></div>
      <div class="room room-bed2" role="img" aria-label="Photo of the master bedroom"></div>
      <div class="room room-spa" role="img" aria-label="Photo of the jetted bathtub"></div>
      <div class="room room-bed3" role="img" aria-label="Photo of a guest bedroom"></div>
    </section>

    <div class="ranking">
      <span>ranked #1 on</span>
      <span class="dot"></span>
      <span class="brand">staywander</span>
    </div>

    <section class="booking">
      <p>Come and enjoy your best ski holiday ever - to secure your place in the Rockies: Email: bellwood5e@examplemail.net or call the Bellwood direct on +1 555-014-2525 and ask for Condo5E for a special rate.</p>
      <p class="tour">For a virtual tour visit: http://www.vidloop.net/watch?v=Q_kkwaPnmRT&amp;feature=vl.be</p>
    </section>
  </main>
</body>
</html>
```